Verdant Loop Advisors, LLC

I am looking for a simple, clear layout with my logo prominent and embossed, on the best quality card stock available. I would like the business name and phone number included on the card as well......I dont want my name anywhere on the card and I would like my logo embossed on the card......something simple with a white back......open to designs as long as they go along with recycling symbols and green type stuff.....The address, website, cell number, fax number, and email are listed below

5374 Tillbury Fenwood Road
Hyattsville, MD 20785

c. 240.555.0143 f. 240.555.0187
e. sales@verdantloopadvisors.example
w. www.verdantloopadvisors.example

Industry/Entity Type

Recycling

```html
<!DOCTYPE html>
<html lang="en">
<head>
<meta charset="utf-8">
<title>Verdant Loop Advisors, LLC — Business Card</title>
<link rel="stylesheet" href="https://fonts.googleapis.com/css2?family=Montserrat:wght@800&family=Open+Sans:wght@400;600&display=swap">
<style>
  :root {
    --backdrop: #7dfcaf;
    --card-white: #ffffff;
    --brand-green: #0a6b2f;
    --icon-green: #9be07a;
    --ink: #1a1a1a;
    --contact-text: #ffffff;
  }
  html, body {
    margin: 0;
    width: 1200px;
    height: 900px;
    overflow: hidden;
    background: var(--backdrop);
  }
  .business-card {
    position: absolute;
    left: 75px;
    top: 150px;
    width: 1050px;
    height: 600px;
    background: var(--card-white);
    box-shadow: 0 14px 36px rgba(0, 60, 30, 0.28);
    overflow: hidden;
  }
  .wave-band {
    position: absolute;
    inset: 0;
  }
  .wave-band path { fill: var(--brand-green); }
  .brand-mark {
    position: absolute;
    left: 64px;
    top: 146px;
    width: 44px;
    height: 44px;
    background: var(--brand-green);
  }
  .brand-name {
    position: absolute;
    left: 124px;
    top: 140px;
    margin: 0;
    font-family: "Montserrat", sans-serif;
    font-weight: 800;
    font-size: 50px;
    line-height: 1.04;
    letter-spacing: 0.5px;
    text-transform: uppercase;
    color: var(--brand-green);
  }
  .address {
    position: absolute;
    left: 66px;
    top: 268px;
    margin: 0;
    font-family: "Open Sans", sans-serif;
    font-size: 20px;
    color: var(--ink);
    white-space: nowrap;
  }
  .contact-list {
    position: absolute;
    left: 655px;
    top: 215px;
    margin: 0;
    padding: 0;
    list-style: none;
    font-family: "Open Sans", sans-serif;
    font-size: 19px;
    color: var(--contact-text);
    white-space: nowrap;
  }
  .contact-item {
    display: flex;
    align-items: center;
    gap: 11px;
    height: 38px;
  }
  .contact-icon {
    width: 18px;
    height: 18px;
    flex: none;
  }
  .contact-icon * {
    fill: none;
    stroke: var(--icon-green);
    stroke-width: 2;
    stroke-linecap: round;
    stroke-linejoin: round;
  }
</style>
</head>
<body>
  <article class="business-card">
    <svg class="wave-band" viewBox="0 0 1050 600" width="1050" height="600" aria-hidden="true">
      <path d="M0,515 H410 C530,515 550,400 590,280 C630,150 740,50 1050,0 V600 H0 Z"/>
    </svg>

    <div class="brand-mark" aria-hidden="true"></div>
    <h1 class="brand-name">Verdant Loop<br>Advisors, LLC</h1>
    <p class="address">5374 Tillbury Fenwood Road Hyattsville, MD 20785</p>

    <ul class="contact-list">
      <li class="contact-item">
        <svg class="contact-icon" viewBox="0 0 20 20" aria-hidden="true"><path d="M5 2 L8 6 L6 8 C7 11 9 13 12 14 L14 12 L18 15 L16 18 C9 18 2 11 2 4 Z"/></svg>
        <span>(240) 555-0143</span>
      </li>
      <li class="contact-item">
        <svg class="contact-icon" viewBox="0 0 20 20" aria-hidden="true"><rect x="3" y="8" width="14" height="9"/><path d="M6 8 V3 H14 V8 M6 12 H14"/></svg>
        <span>(240) 555-0187</span>
      </li>
      <li class="contact-item">
        <svg class="contact-icon" viewBox="0 0 20 20" aria-hidden="true"><rect x="2" y="4" width="16" height="12"/><path d="M2 4 L10 11 L18 4"/></svg>
        <span>sales@verdantloopadvisors.example</span>
      </li>
      <li class="contact-item">
        <svg class="contact-icon" viewBox="0 0 20 20" aria-hidden="true"><circle cx="10" cy="10" r="8"/><path d="M2 10 H18 M10 2 C6 6 6 14 10 18 M10 2 C14 6 14 14 10 18"/></svg>
        <span>www.verdantloopadvisors.example</span>
      </li>
    </ul>
  </article>
</body>
</html>
```